Sports Photography Business Cards

I recently started a small photography business, mainly school sports photography. I already have a logo, but I am looking for business cards to get more people to my website and be able to contact me easily. I also have a QR code (which brings you to my site) that I would like to include on the card. I want to include my phone number, email, Instagram link, and website address.
I love the colors green and pink, but I am not 100% committed to any. I would love to have foil on my cards, but it is not a deal breaker.
The final design should be clean, easy to read, and eye catching.
Target Market(s)
Parents
Industry/Entity Type
Photography
Contact Information for Business Card
Phone Number, Email, Website, QR Code
Look and feel
Each slider illustrates characteristics of the customer's brand and the style your logo design should communicate.

```html
<!DOCTYPE html>
<html lang="en">
<head>
<meta charset="utf-8">
<title>Nora B. Lindell Photography — Business Card</title>
<link rel="stylesheet" href="https://fonts.googleapis.com/css2?family=Cinzel:wght@500&family=Cormorant+Garamond:wght@500&family=Lato:wght@300;400&display=swap">
<style>
  :root {
    --green: #17705e;
    --green-deep: #0b3d33;
    --green-mid: #1c6b58;
    --pink: #d98aa8;
    --paper: #ffffff;
    --backdrop: #e9e7e3;
    --white: #ffffff;
  }
  * { box-sizing: border-box; margin: 0; padding: 0; }
  html, body { width: 1200px; height: 960px; overflow: hidden; }
  body {
    background: var(--backdrop);
    font-family: 'Lato', sans-serif;
    position: relative;
  }
  .card {
    position: absolute;
    left: 250px;
    width: 700px;
    height: 400px;
    border-radius: 4px;
    box-shadow: 0 8px 24px rgba(0,0,0,0.18);
    overflow: hidden;
  }
  .card--front { top: 50px; background: var(--paper); }
  .card--back { top: 510px; }

  /* front */
  .brand {
    position: absolute; top: 58px; left: 0; right: 0;
    display: flex; align-items: center; justify-content: center; gap: 14px;
  }
  .brand__circle {
    width: 54px; height: 54px; border-radius: 50%;
    border: 2px solid var(--green);
  }
  .brand__name {
    font-family: 'Lato', sans-serif; font-weight: 400;
    font-size: 30px; color: var(--green); letter-spacing: 1px;
  }
  .divider {
    position: absolute; top: 178px; height: 2px; background: var(--green);
  }
  .divider--left { left: 36px; width: 190px; }
  .divider--right { right: 36px; width: 190px; }
  .title {
    position: absolute; top: 150px; left: 0; right: 0; text-align: center;
    font-family: 'Cinzel', serif; font-weight: 500;
    font-size: 26px; letter-spacing: 3px; color: var(--green);
  }
  .subtitle {
    position: absolute; top: 184px; left: 0; right: 0; text-align: center;
    font-family: 'Cormorant Garamond', serif; font-weight: 500;
    font-size: 20px; letter-spacing: 1px; color: var(--green);
  }
  .icons {
    position: absolute; top: 222px; left: 0; right: 0;
    display: flex; justify-content: center; gap: 10px;
  }
  .icons svg { width: 20px; height: 20px; }
  .contacts {
    position: absolute; top: 254px; left: 0; right: 0;
    list-style: none; text-align: center;
    font-size: 19px; line-height: 26px; color: var(--green);
  }

  /* back */
  .card--back .pattern {
    position: absolute; inset: 0;
    background: radial-gradient(ellipse at 35% 25%, var(--green-mid) 0%, var(--green-deep) 80%);
  }
  .back-brand {
    position: absolute; top: 110px; left: 0; right: 0;
    display: flex; flex-direction: column; align-items: center; gap: 18px;
  }
  .back-brand__row { display: flex; align-items: center; gap: 16px; }
  .back-brand__circle {
    width: 64px; height: 64px; border-radius: 50%;
    border: 2px solid var(--white);
  }
  .back-brand__name {
    font-weight: 300; font-size: 40px; color: var(--white); letter-spacing: 1px;
  }
  .back-brand__tag {
    font-weight: 300; font-size: 26px; letter-spacing: 6px; color: var(--white);
  }
</style>
</head>
<body>
  <section class="card card--front">
    <div class="brand">
      <span class="brand__circle"></span>
      <span class="brand__name">Nora B. Lindell</span>
    </div>
    <div class="divider divider--left"></div>
    <div class="divider divider--right"></div>
    <h1 class="title">ARMY VETERAN</h1>
    <p class="subtitle">Photographer</p>
    <div class="icons">
      <svg viewBox="0 0 20 20" aria-label="Phone"><rect x="5" y="1" width="10" height="18" rx="2" fill="none" stroke="var(--pink)" stroke-width="2"/><circle cx="10" cy="15.5" r="1.2" fill="var(--pink)"/></svg>
      <svg viewBox="0 0 20 20" aria-label="Email"><rect x="1" y="4" width="18" height="12" fill="var(--pink)"/><path d="M1 4 L10 11 L19 4" fill="none" stroke="var(--paper)" stroke-width="1.5"/></svg>
      <svg viewBox="0 0 20 20" aria-label="Social"><rect x="2" y="2" width="16" height="16" rx="4" fill="var(--pink)"/></svg>
      <svg viewBox="0 0 20 20" aria-label="Website"><circle cx="10" cy="10" r="8.5" fill="var(--pink)"/><path d="M1.5 10 H18.5 M10 1.5 V18.5 M4 5 H16 M4 15 H16" stroke="var(--paper)" stroke-width="1"/><ellipse cx="10" cy="10" rx="4" ry="8.5" fill="none" stroke="var(--paper)" stroke-width="1"/></svg>
    </div>
    <ul class="contacts">
      <li>555-014-2290</li>
      <li>info@noralindellphoto</li>
      <li>@noralindell.photo</li>
      <li>www.noralindellphoto.example.com</li>
    </ul>
  </section>

  <section class="card card--back">
    <div class="pattern" role="img" aria-label="Dark green background with a faint repeated monogram pattern"></div>
    <div class="back-brand">
      <div class="back-brand__row">
        <span class="back-brand__circle"></span>
        <span class="back-brand__name">Nora B. Lindell</span>
      </div>
      <span class="back-brand__tag">PHOTOGRAPHY</span>
    </div>
  </section>
</body>
</html>
```